author needs a Book Cover design

Needs a book cover design that matches the title in some way.
Book Title is- 9 Lanterns Beyond the Quiet Harbor at Dusk.
Subtile- Gentle Lessons On Morning Gardens.
Author Name:-Gordon Peltiway, Sr.

Final Design is subject to Book Publisher's requirement.

Font styles to use
Serif

Requirements
Must have
• Follow these recommended specifications for your cover file:
• Page Size: Your cover should be a single (one-piece) PDF that includes the back cover, spine, and front cover. You can submit your cover on any size page as long as the printable area is measured exactly for your book's trim size, spine width, and allows at least .125” bleed, centered horizontally and vertically.
• Minimum Cover Width: Bleed + Back Cover Trim Size + Spine Width + Front Cover Trim Size + Bleed
• Minimum Cover Height: Bleed + Book Height Trim Size + Bleed
• Trim Size: Your cover should be the same trim size as you choose in the Title Information when setting up your book. For example, submitting a cover that was previously used for a 6.25” x 9.25” book would not work for a 6” x 9” book.
• Barcodes: For manufacturing and distribution reasons, your book's back cover must include a valid ISBN barcode. If your cover already has an ISBN barcode, make sure it is high-resolution, or at least 300 dpi, and 1.5" - 2" in width with proportional height. Ideally, this barcode should be 2” wide by 1.2” tall. Also, check to make sure you have the rights to use the ISBN on your cover, because not all services allow you to use their ISBNs elsewhere.
• QR codes: There are no set size restrictions, but the quality (resolution) of the image must be set to at least 300 dpi. Make sure you have the rights to use the code.
• If your artwork does not include a barcode, we will automatically add one in the lower right-hand corner of your book's back cover, free of charge. Our system will place the ISBN barcode in a space 2" wide and 1.2" tall. The bottom of this barcode is located 1/4" up from the bottom trim line of the cover. The right side of the barcode is located 1/4" to the left of the spine. Please ensure that you don't have any important images or text in the barcode location. You can also refer to our Artwork Templates for the exact size and position of the ISBN barcode on your final cover.
• If you don’t have an ISBN already on your cover, but you have live graphic or text elements in the location that our system will place the ISBN, you will need to move those elements or place the ISBN in a different location yourself.
• Publishing Logos: We do not add our logo to your book.
• Spine Width and Variance: If your artwork was created for a different service, please make sure that the spine width of your current cover matches our spine width. Different services may use different paper thickness, which is why the spine width of your cover artwork could be correct for another service but incorrect for our service.
• Ideally, you should avoid hard vertical lines separating your front or back cover panels from your spine and should allow for at least a .125" variance of your spine on each side (for example, the text on a 1" spine should be no larger than .75" wide). For books with a page count of less than 130 pages, we strongly recommend a blank spine.
• Your spine width should be calculated based on the number of pages in your book and using the appropriate formula:
• Black and White Interior Book Spine Width:
• White paper: Number of pages x .002252 = Spine width in inches
• Cream paper: Number of pages x .0025 = Spine width in inches
• Color Interior Book Spine Width:
• Number of pages x .002347 = Spine width in inches
• Example of spine width calculation for a 120-page black and white interior book with white paper:
• 120 x .002252 = .27" spine width
• Text and Image Placement: All live cover elements, or text and images that cannot be cut, must be at least .125" inside the trim lines to ensure no important elements are cut during the bookmaking process and the appearance of your printed books is consistent.
• Bleed: Your cover's background must extend at least .125" beyond the final trim line to accommodate for cutting/trimming tolerance.
• Crop/Registration Marks: Please do not include any crop or registration marks on your files, as they may interfere with the binding process or appear on the cover. We use our own measurements, specific to our systems, for cutting and binding; crop or registration marks placed by you could interfere with this process.
• Images and Fonts: Any images you include on your book's cover may be tagged with your choice of CMYK or RGB profiles or left untagged in a generic color space. All images should be sized at 100%, flattened to one layer and placed in your native document at a resolution of at least 300 DPI. You should also embed all fonts in your PDF file.
• Gordon, I hope this information is helpful to you. Please feel free to contact us if you have any other questions or concerns.
• Best regards,
• *WILL SUPPLY THE PAGE NUMBERS INFORMATION
• Lenora
• PrintHollow Member Services
Nice to have
• An attractive design that matches the title. Design can include backgrounds

```html
<!DOCTYPE html>
<html lang="en">
<head>
<meta charset="utf-8">
<title>9 Lanterns Beyond the Quiet Harbor at Dusk — Book Cover</title>
<link rel="stylesheet" href="https://fonts.googleapis.com/css2?family=Cinzel:wght@400;500&family=Cormorant+Garamond:ital,wght@1,500&family=Libre+Baskerville:wght@700&display=swap">
<style>
  :root {
    --page-bg: #ffffff;
    --sky-top: #14244f;
    --sky-mid: #3d5c97;
    --sky-haze: #8ea3c4;
    --horizon-glow: #f7d79a;
    --horizon-warm: #f0a860;
    --horizon-ember: #d9642e;
    --water-rose: #c98f98;
    --water-violet: #7d6a99;
    --water-deep: #1b2446;
    --ink-light: #ffffff;
    --ink-soft: #eef1f8;
  }
  * { margin: 0; padding: 0; box-sizing: border-box; }
  html, body {
    width: 1200px;
    height: 1019px;
    overflow: hidden;
    background: var(--page-bg);
  }
  .canvas {
    position: relative;
    width: 1200px;
    height: 1019px;
    background: var(--page-bg);
  }
  .front-cover {
    position: absolute;
    left: 0;
    top: 0;
    width: 689px;
    height: 1019px;
    overflow: hidden;
  }
  .cover-art {
    position: absolute;
    inset: 0;
    width: 100%;
    height: 100%;
    display: block;
  }
  .title-block {
    position: absolute;
    left: 0;
    right: 0;
    top: 54px;
    text-align: center;
    color: var(--ink-light);
    text-shadow: 0 2px 6px rgba(10, 20, 50, 0.35);
  }
  .title-main {
    font-family: "Cinzel", serif;
    font-weight: 400;
    font-size: 104px;
    line-height: 1;
    letter-spacing: 1px;
    white-space: nowrap;
  }
  .title-line {
    font-family: "Cinzel", serif;
    font-weight: 400;
    line-height: 1.05;
    white-space: nowrap;
  }
  .title-line--short {
    margin-top: 12px;
    font-size: 50px;
    letter-spacing: 1px;
  }
  .title-line--long {
    margin-top: 2px;
    font-size: 46px;
    letter-spacing: 0.5px;
  }
  .subtitle {
    margin-top: 18px;
    font-family: "Cormorant Garamond", serif;
    font-style: italic;
    font-weight: 500;
    font-size: 27px;
    font-variant: small-caps;
    letter-spacing: 0.5px;
    color: var(--ink-soft);
    white-space: nowrap;
  }
  .author {
    position: absolute;
    left: 0;
    right: 0;
    bottom: 22px;
    text-align: center;
    font-family: "Libre Baskerville", serif;
    font-weight: 700;
    font-size: 27px;
    letter-spacing: 2px;
    color: var(--ink-light);
    white-space: nowrap;
  }
</style>
</head>
<body>
<main class="canvas">
  <section class="front-cover">
    <svg class="cover-art" viewBox="0 0 689 1019" preserveAspectRatio="none" role="img" aria-label="Cover illustration: two figures standing in calm shallow water beneath a starry blue sky, facing a glowing orange sunset on the horizon, one with arms raised">
      <defs>
        <linearGradient id="sky-gradient" x1="0" y1="0" x2="0" y2="1">
          <stop offset="0" stop-color="var(--sky-top)"/>
          <stop offset="0.3" stop-color="var(--sky-mid)"/>
          <stop offset="0.45" stop-color="var(--sky-haze)"/>
          <stop offset="0.55" stop-color="var(--horizon-glow)"/>
          <stop offset="0.62" stop-color="var(--horizon-warm)"/>
          <stop offset="0.72" stop-color="var(--water-rose)"/>
          <stop offset="0.86" stop-color="var(--water-violet)"/>
          <stop offset="1" stop-color="var(--water-deep)"/>
        </linearGradient>
        <radialGradient id="sun-glow" cx="0.5" cy="0.56" r="0.5">
          <stop offset="0" stop-color="#fff3cf" stop-opacity="0.9"/>
          <stop offset="0.35" stop-color="var(--horizon-glow)" stop-opacity="0.5"/>
          <stop offset="1" stop-color="var(--horizon-glow)" stop-opacity="0"/>
        </radialGradient>
        <radialGradient id="ember-glow" cx="0.95" cy="0.6" r="0.45">
          <stop offset="0" stop-color="var(--horizon-ember)" stop-opacity="0.75"/>
          <stop offset="1" stop-color="var(--horizon-ember)" stop-opacity="0"/>
        </radialGradient>
      </defs>
      <rect width="689" height="1019" fill="url(#sky-gradient)"/>
      <rect width="689" height="1019" fill="url(#ember-glow)"/>
      <rect width="689" height="1019" fill="url(#sun-glow)"/>
    </svg>

    <header class="title-block">
      <h1 class="title-main">9 LANTERNS</h1>
      <p class="title-line title-line--short">Beyond the</p>
      <p class="title-line title-line--long">Quiet Harbor at Dusk</p>
      <p class="subtitle">Gentle Lessons On Morning Gardens</p>
    </header>

    <p class="author">GORDON PELTIWAY, SR.</p>
  </section>
</main>
</body>
</html>
```